Quarlwick Builders Business Cards

I want to use the logo and make an unique business card that shows the textured Logo with brick and builings. I want to be able to stand out when I pass out business cards.

```html
<!DOCTYPE html>
<html lang="en">
<head>
<meta charset="utf-8">
<title>Quarlwick Builders Business Card</title>
<link href="https://fonts.googleapis.com/css2?family=Montserrat:wght@400;500;700;800&family=Oswald:wght@500&display=swap" rel="stylesheet">
<style>
  :root {
    --page-bg: #3a3a3c;
    --concrete-light: #9a9b92;
    --concrete-mid: #75766f;
    --concrete-dark: #45463f;
    --concrete-stain: #5c5d56;
    --accent: #f0542a;
    --ink: #1c1c1c;
    --navy: #14254a;
    --glow: rgba(235, 235, 225, .55);
  }
  * { margin: 0; padding: 0; box-sizing: border-box; }
  html, body {
    width: 1200px; height: 988px; overflow: hidden;
    background: var(--page-bg);
  }
  .card {
    position: absolute; left: 100px; top: 208px;
    width: 1000px; height: 572px;
    border-radius: 30px;
    background:
      radial-gradient(ellipse 60% 70% at 0% 50%, rgba(40,40,36,.55), transparent 70%),
      radial-gradient(ellipse 55% 60% at 100% 100%, rgba(40,40,36,.6), transparent 70%),
      radial-gradient(ellipse 40% 30% at 30% 8%, rgba(220,220,210,.35), transparent 70%),
      radial-gradient(ellipse 25% 35% at 70% 45%, rgba(70,70,64,.35), transparent 70%),
      radial-gradient(ellipse 30% 25% at 18% 78%, rgba(80,80,72,.35), transparent 70%),
      radial-gradient(ellipse 22% 18% at 85% 20%, rgba(200,200,190,.25), transparent 70%),
      radial-gradient(ellipse 70% 80% at 38% 42%, var(--concrete-light) 0%, var(--concrete-mid) 55%, var(--concrete-dark) 100%);
    box-shadow: 0 6px 0 var(--accent), 0 24px 40px rgba(0,0,0,.45);
    overflow: hidden;
    font-family: "Montserrat", sans-serif;
    color: var(--ink);
  }
  .brand {
    position: absolute; left: 30px; top: 110px; width: 440px; height: 330px;
    display: flex; align-items: center; justify-content: center; gap: 16px;
  }
  .brand-mark { width: 34px; height: 34px; background: var(--accent); flex: none; }
  .brand-name {
    font-weight: 800; font-size: 52px; line-height: 1.05;
    color: var(--accent); text-transform: uppercase;
  }
  .services {
    position: absolute; left: 30px; bottom: 60px; width: 450px;
    text-align: center; white-space: nowrap;
    font-family: "Oswald", sans-serif; font-weight: 500;
    font-size: 21px; color: var(--navy);
    text-shadow: 0 0 8px var(--glow);
  }
  .divider {
    position: absolute; left: 490px; top: 130px;
    width: 3px; height: 330px; background: var(--accent);
  }
  .details { position: absolute; left: 530px; top: 70px; right: 30px; }
  .person-name {
    font-weight: 800; font-size: 40px; color: var(--accent); letter-spacing: .5px;
    text-shadow: 0 0 10px var(--glow);
  }
  .person-title, .address, .contact-list li { text-shadow: 0 0 8px var(--glow); }
  .person-title { font-size: 20px; margin-top: 2px; }
  .address { font-size: 21px; line-height: 1.3; margin-top: 34px; padding-left: 50px; }
  .contact-list { list-style: none; margin-top: 22px; padding-left: 50px; }
  .contact-list li {
    display: flex; align-items: center; gap: 12px;
    font-size: 21px; line-height: 1.5; white-space: nowrap;
  }
  .contact-list svg { width: 18px; height: 18px; flex: none; fill: var(--accent); }
</style>
</head>
<body>
  <div class="card">
    <div class="brand">
      <span class="brand-mark"></span>
      <span class="brand-name">Quarlwick<br>Builders</span>
    </div>
    <p class="services">Patios - Sidewalks - Retaining Walls - Foundations</p>

    <div class="divider"></div>

    <div class="details">
      <h1 class="person-name">Dorian Velkamp</h1>
      <p class="person-title">Partner, Chief Officer</p>
      <p class="address">42 Brantel Crescent,<br>Suite 210<br>Norvale, ON K9T 4P7</p>
      <ul class="contact-list">
        <li><svg viewBox="0 0 24 24"><path d="M6.6 10.8a15 15 0 0 0 6.6 6.6l2.2-2.2c.3-.3.7-.4 1-.2 1.1.4 2.3.6 3.6.6.6 0 1 .4 1 1V20c0 .6-.4 1-1 1A17 17 0 0 1 3 4c0-.6.4-1 1-1h3.5c.6 0 1 .4 1 1 0 1.3.2 2.5.6 3.6.1.3 0 .7-.2 1z"/></svg>555-201-3348</li>
        <li><svg viewBox="0 0 24 24"><path d="M7 2h10a2 2 0 0 1 2 2v16a2 2 0 0 1-2 2H7a2 2 0 0 1-2-2V4a2 2 0 0 1 2-2zm0 3v13h10V5zm5 14.2a1 1 0 1 0 0 .1z"/></svg>555-307-8812</li>
        <li><svg viewBox="0 0 24 24"><path d="M3 5h18v14H3zm2 2v.5l7 4.5 7-4.5V7zm0 3v7h14v-7l-7 4.5z"/></svg>dorian.velkamp@halvorinc.com</li>
        <li><svg viewBox="0 0 24 24"><path d="M12 2a10 10 0 1 0 0 20 10 10 0 0 0 0-20zm6.9 9h-3a15 15 0 0 0-1.4-6A8 8 0 0 1 18.9 11zM12 4c.9 1.2 1.8 3.6 1.9 7h-3.8c.1-3.4 1-5.8 1.9-7zM9.5 5a15 15 0 0 0-1.4 6h-3A8 8 0 0 1 9.5 5zM5.1 13h3a15 15 0 0 0 1.4 6A8 8 0 0 1 5.1 13zM12 20c-.9-1.2-1.8-3.6-1.9-7h3.8c-.1 3.4-1 5.8-1.9 7zm2.5-1a15 15 0 0 0 1.4-6h3a8 8 0 0 1-4.4 6z"/></svg>www.halvorinc.com</li>
      </ul>
    </div>
  </div>
</body>
</html>
```